Website for Brisbeck Current Glide

Require a website for a river float in the City of Edmonton. Located on North Saskatchewan River. Will need to be a coded website with incorporated booking system through Fare Harbor software.

Pages include
Home
Pricing
About
FAQ
Contact

Brisbeck Current Glide is an activity based business that will have customers floating down the North Saskatchewan river in Edmonton AB. The site will have all information needed and a full reservation system. The project was launched to provide people in the Edmonton area a favorite summer activity.

Here are similar websites to reference what our business will be doing and what we are looking for.

mellowbendcanoehire.example
pinegulchloopers.example

Target Market(s)

Families, Groups, Individuals, Anyone who wants to explore the river

Industry/Entity Type

Activities based business/ Outdoor recreational/ River Float

Coding

Coded - Design and coding required

Number of Pages Required

5+ page

Colors
0054AA
0677BA
7BADD7
CADEEF
E8F1F8
F0912C
F2A743
F7CA91
FBE8D2
FDF5EE

```html
<!DOCTYPE html>
<html lang="en">
<head>
<meta charset="utf-8">
<title>Brisbeck Current Glide</title>
<link rel="stylesheet" href="https://fonts.googleapis.com/css2?family=Poppins:wght@400;500;600;700&display=swap">
<style>
:root{
  --navy:#0b2e67;
  --navy-text:#0d3a72;
  --blue:#0e55ad;
  --sky:#7badd7;
  --cyan:#4cc3ea;
  --white:#ffffff;
  --frame-shadow:rgba(10,40,90,.12);
  --rule:rgba(255,255,255,.35);
}
*{box-sizing:border-box;margin:0;padding:0}
html,body{width:1200px;height:2438px;overflow:hidden;background:var(--white)}
body{position:relative;font-family:"Poppins",sans-serif;color:var(--navy-text)}
a{color:inherit;text-decoration:none}

.hero{position:absolute;left:0;top:0;width:1200px;height:562px;
  background:linear-gradient(180deg,#eae6ea 0%,#dcd6d8 22%,#b9b0a4 36%,#5d7a45 52%,#5b7d86 62%,#7d9ca4 75%,#5f7f55 100%)}
.hero-brand{position:absolute;left:86px;top:22px;display:flex;align-items:center;gap:8px}
.hero-brand .dot{width:30px;height:30px;border-radius:50%;background:var(--cyan)}
.hero-brand span{font-weight:700;font-size:15px;color:var(--navy);line-height:1.1;width:92px}
.main-nav{position:absolute;right:87px;top:48px;display:flex;gap:28px;font-size:15px;font-weight:500;color:var(--navy)}
.main-nav a.current{border-bottom:2px solid var(--navy);padding-bottom:2px}
.hero-tag{position:absolute;left:87px;top:226px;height:33px;padding:0 16px;background:var(--navy);color:var(--white);font-size:15.5px;line-height:33px;white-space:nowrap}
.hero-title{position:absolute;left:83px;top:262px;font-size:64px;font-weight:700;color:var(--white);letter-spacing:-.5px;white-space:nowrap;text-shadow:0 2px 6px rgba(0,0,0,.35)}

.btn{position:absolute;display:flex;height:59px;font-size:16px;font-weight:500;color:var(--white);white-space:nowrap}
.btn .label{background:var(--navy);display:flex;align-items:center;justify-content:center;flex:0 0 auto}
.btn .icon{background:var(--blue);display:flex;align-items:center;justify-content:center;flex:0 0 auto}
.hero-btn{left:86px;top:352px}
.hero-btn .label{width:129px}
.hero-btn .icon{width:50px}
.wide-btn .label{width:129px}
.wide-btn .icon{width:61px}

.scroll-cue{position:absolute;left:577px;top:529px;width:46px;height:66px;border-radius:23px;background:var(--white);box-shadow:0 3px 8px rgba(0,0,0,.12);display:flex;align-items:center;justify-content:center}

.frame{position:absolute;background:var(--white);padding:13px;box-shadow:0 2px 12px var(--frame-shadow)}
.frame .photo{width:100%;height:100%}
.shuttle-frame{left:86px;top:673px;width:526px;height:436px}
.shuttle-frame .photo{background:linear-gradient(135deg,#9a9a9a 0%,#e6e6e6 35%,#bdbdbd 60%,#4c4c4c 100%)}
.shuttle-copy{position:absolute;left:665px;top:731px;width:460px}
.shuttle-copy h2{font-size:39px;font-weight:600;line-height:1.15;color:var(--navy)}
.shuttle-copy p{margin-top:30px;font-size:16px;line-height:25px;letter-spacing:-.1px}
.shuttle-copy .btn{position:relative;margin-top:27px}

.week-title{position:absolute;left:0;width:1200px;top:1210px;text-align:center;font-size:39px;font-weight:600;color:var(--navy)}
.float-frame{left:86px;top:1294px;width:1028px;height:415px}
.float-frame .photo{background:linear-gradient(180deg,#a8a777 0%,#6d7d3e 35%,#9da38c 55%,#d8ddd4 75%,#e9ecea 100%)}
.week-copy{position:absolute;left:130px;width:940px;top:1738px;text-align:center;font-size:16px;line-height:25px;letter-spacing:-.1px}
.week-btn{left:504px;top:1837px}

.site-footer{position:absolute;left:0;top:2007px;width:1200px;height:431px;background:var(--navy);color:var(--white)}
.col{position:absolute;text-align:center}
.col h3{font-size:19px;font-weight:600}
.col h3::after{content:"";display:block;width:28px;height:2px;background:var(--white);margin:12px auto 0}
.connect{left:46px;width:400px;top:90px;font-size:16px;line-height:28px}
.connect h3{margin-bottom:22px}
.connect b{font-weight:600}
.socials{display:flex;gap:11px;justify-content:center;margin:18px 0 14px}
.socials span{width:44px;height:44px;border-radius:6px;background:rgba(255,255,255,.18)}
.connect .signup{color:var(--cyan);font-weight:600}
.footer-brand{left:450px;width:300px;top:82px}
.footer-brand .dot{width:150px;height:150px;border-radius:50%;background:var(--cyan);margin:0 auto}
.footer-brand .name{font-size:26px;font-weight:700;margin-top:8px;line-height:1.1}
.footer-brand p{font-size:16px;margin-top:10px}
.footer-nav{left:798px;width:300px;top:90px;font-size:16px}
.footer-nav h3{margin-bottom:18px}
.footer-nav a{display:block;line-height:38.5px}
.footer-rule{position:absolute;left:86px;width:1028px;top:365px;height:1px;background:var(--rule)}
.copyright{position:absolute;left:0;width:1200px;top:381px;text-align:center;font-size:16px}
</style>
</head>
<body>

<header class="hero" role="img" aria-label="Downtown skyline above a river with a bridge and green banks">
  <div class="hero-brand"><div class="dot"></div><span>Brisbeck Current Glide</span></div>
  <nav class="main-nav">
    <a class="current" href="#">HOME</a><a href="#">PRICING</a><a href="#">ABOUT</a><a href="#">FAQ</a><a href="#">CONTACT</a>
  </nav>
  <div class="hero-tag">Float the North Saskatchewan through downtown Edmonton</div>
  <h1 class="hero-title">BRISBECK CURRENT GLIDE</h1>
  <a class="btn hero-btn" href="#"><span class="label">Book Now</span><span class="icon"><svg width="14" height="16" viewBox="0 0 14 16"><path d="M1 1 L13 8 L1 15Z" fill="#fff"/></svg></span></a>
  <div class="scroll-cue"><svg width="20" height="12" viewBox="0 0 20 12"><path d="M2 2 L10 10 L18 2" fill="none" stroke="#0b2e67" stroke-width="2"/></svg></div>
</header>

<div class="frame shuttle-frame"><div class="photo" role="img" aria-label="Row of white shuttle vans parked beside trees"></div></div>
<section class="shuttle-copy">
  <h2>Shuttle Service And Gear Included</h2>
  <p>We provide everything you need including round trip shuttle service, float tube, lifejacket, paddle, and more. Fun for everyone!</p>
  <a class="btn wide-btn" href="#"><span class="label">Learn More</span><span class="icon"><svg width="28" height="10" viewBox="0 0 28 10"><path d="M0 5 H26 M21 1 L26 5 L21 9" fill="none" stroke="#fff" stroke-width="1.6"/></svg></span></a>
</section>

<h2 class="week-title">Floating 7 &amp; Days A Week</h2>
<div class="frame float-frame"><div class="photo" role="img" aria-label="Friends in life jackets paddling kayaks on a calm river"></div></div>
<p class="week-copy">Our priority is to make sure everyone has a safe and fun time on the river. Safety demonstrations are provided and staff are available to assist in any way. Whether you are a family with children, larger group or just want a relaxing way to explore the river, this is a must try activity.</p>
<a class="btn wide-btn week-btn" href="#"><span class="label">Book Now</span><span class="icon"><svg width="28" height="10" viewBox="0 0 28 10"><path d="M0 5 H26 M21 1 L26 5 L21 9" fill="none" stroke="#fff" stroke-width="1.6"/></svg></span></a>

<footer class="site-footer">
  <div class="col connect">
    <h3>Connect</h3>
    <div><b>EMAIL:</b> info@brisbeckcurrentglide.example</div>
    <div><b>LOCATION:</b> Willowmere Landing</div>
    <div class="socials"><span></span><span></span><span></span></div>
    <div><a class="signup" href="#">Sign up</a> for our mailing list</div>
  </div>
  <div class="col footer-brand">
    <div class="dot"></div>
    <div class="name">Brisbeck Current Glide</div>
    <p>Floating 7 days a week</p>
  </div>
  <nav class="col footer-nav">
    <h3>Main Navigation</h3>
    <a href="#">Home</a><a href="#">Pricing</a><a href="#">About</a><a href="#">FAQ</a><a href="#">Contact</a>
  </nav>
  <div class="footer-rule"></div>
  <div class="copyright">Copyright 2022.Brisbeck Current Glide.All right reserved.</div>
</footer>

</body>
</html>
```